Letterhead and Business card for Brevon Logistics
Brevon Logistics
Letterhead and Business card for Brevon Logistics - Transportation
Creative Brief
Professional
Dirk Makhanya
Manager
17 Kolbe Street Meriton Calderwood Harlen 0420
dirk@brevonlogistics.example

```html
<!DOCTYPE html>
<html lang="en">
<head>
<meta charset="utf-8">
<title>Brevon Logistics – Stationery Set</title>
<link href="https://fonts.googleapis.com/css2?family=Montserrat:wght@400;600;700&family=Playfair+Display:wght@400&display=swap" rel="stylesheet">
<style>
  :root {
    --backdrop: #a9a9a9;
    --paper: #ffffff;
    --ink: #1c1c1c;
    --ink-soft: #8a8a8a;
    --rule: #d6d6d6;
    --card-dark: #141414;
    --window: #2a2a2a;
  }
  * { box-sizing: border-box; margin: 0; padding: 0; }
  html, body { width: 1200px; height: 350px; overflow: hidden; }
  body {
    background: var(--backdrop);
    font-family: "Montserrat", Arial, sans-serif;
    color: var(--ink);
    position: relative;
  }
  .piece { position: absolute; background: var(--paper); box-shadow: 0 2px 5px rgba(0,0,0,.2); }

  .brand { display: flex; align-items: center; gap: 4px; font-weight: 700; white-space: nowrap; }
  .brand-mark { display: inline-block; background: currentColor; flex: none; }

  /* Business cards */
  .card { width: 86px; height: 48px; }
  .card-front { left: 24px; top: 174px; background: var(--card-dark); color: var(--paper);
    display: flex; align-items: center; justify-content: center; }
  .card-front .brand { font-size: 7px; gap: 3px; }
  .card-front .brand-mark { width: 6px; height: 6px; }
  .card-back { left: 24px; top: 232px; padding: 6px 7px; }
  .card-back .brand { font-size: 5px; gap: 3px; }
  .card-back .brand-mark { width: 4px; height: 4px; }
  .card-details { margin-top: 8px; font-size: 3px; line-height: 1.4; white-space: nowrap; }
  .card-name { font-weight: 700; font-size: 4px; }
  .card-title { color: var(--ink-soft); }

  /* Letterhead */
  .letterhead { left: 151px; top: 26px; width: 168px; height: 286px; padding: 13px 13px; }
  .letterhead-top { display: flex; justify-content: space-between; align-items: flex-start; }
  .letterhead .brand { font-size: 7px; gap: 3px; }
  .letterhead .brand-mark { width: 6px; height: 6px; }
  .sender-address { font-size: 3px; line-height: 1.5; text-align: right; color: var(--ink-soft); white-space: nowrap; }
  .headline { margin-top: 26px; font-size: 9px; font-weight: 700; letter-spacing: .3px; }
  .letter-body p { font-size: 3.2px; line-height: 1.65; margin-top: 5px; color: #555; }
  .sign-off { margin-top: 12px; font-size: 3.4px; line-height: 1.5; }
  .signature { font-family: "Playfair Display", Georgia, serif; font-size: 7px; font-style: italic; }
  .letterhead-footer { position: absolute; left: 13px; right: 13px; bottom: 10px;
    border-top: 1px solid var(--rule); padding-top: 3px; font-size: 2.8px; color: var(--ink-soft); text-align: center; white-space: nowrap; }

  /* Envelopes */
  .envelope-back { left: 427px; top: 29px; width: 173px; height: 110px; }
  .envelope-back svg { position: absolute; inset: 0; }
  .envelope-front { left: 396px; top: 173px; width: 228px; height: 110px; padding: 10px 12px; }
  .envelope-front .brand { font-size: 7px; gap: 3px; }
  .envelope-front .brand-mark { width: 6px; height: 6px; }
  .envelope-front .sender-address { text-align: left; margin-top: 3px; }
  .envelope-window { position: absolute; right: 44px; bottom: 22px; width: 66px; height: 30px;
    border-radius: 5px; background: var(--window); }

  /* Notepad */
  .notepad { left: 713px; top: 142px; width: 130px; height: 170px; display: flex; align-items: center; justify-content: center; }
  .notepad-binding { position: absolute; top: -4px; left: 6px; right: 6px; height: 8px;
    background: repeating-linear-gradient(90deg, var(--ink) 0 2px, transparent 2px 5px); }
  .notepad .brand { font-size: 8px; gap: 3px; }
  .notepad .brand-mark { width: 6px; height: 6px; }

  /* Disc */
  .disc { position: absolute; left: 1008px; top: 24px; width: 168px; height: 168px; border-radius: 50%;
    background: var(--card-dark); box-shadow: 0 2px 5px rgba(0,0,0,.25); }
  .disc-hub { position: absolute; left: 50%; top: 50%; width: 40px; height: 40px; margin: -20px 0 0 -20px;
    border-radius: 50%; background: #3a3a3a; }
  .disc-hole { position: absolute; left: 50%; top: 50%; width: 12px; height: 12px; margin: -6px 0 0 -6px;
    border-radius: 50%; background: var(--backdrop); }

  /* ID badge */
  .lanyard { position: absolute; left: 985px; top: 162px; width: 78px; height: 40px;
    border: 2px solid var(--ink); border-bottom: none; border-radius: 40px 40px 0 0; }
  .badge { left: 979px; top: 200px; width: 90px; height: 124px; border: 3px solid var(--card-dark);
    padding: 12px 8px; }
  .badge-clip { position: absolute; top: 4px; left: 50%; width: 18px; height: 3px; margin-left: -9px; border-radius: 2px; background: var(--rule); }
  .badge .card-name { font-family: "Playfair Display", Georgia, serif; font-weight: 400; font-size: 8px; margin-top: 4px; }
  .badge .card-title { font-size: 4px; }
  .badge .brand { position: absolute; left: 8px; bottom: 30px; font-size: 6px; gap: 3px; }
  .badge .brand-mark { width: 5px; height: 5px; }
</style>
</head>
<body>

  <div class="piece card card-front">
    <div class="brand"><span class="brand-mark"></span>Brevon Logistics</div>
  </div>

  <div class="piece card card-back">
    <div class="brand"><span class="brand-mark"></span>Brevon Logistics</div>
    <div class="card-details">
      <div class="card-name">Dirk Makhanya</div>
      <div class="card-title">Manager</div>
      <div>17 Kolbe Street Meriton, Calderwood 0420</div>
      <div>dirk@brevonlogistics.example</div>
    </div>
  </div>

  <div class="piece letterhead">
    <div class="letterhead-top">
      <div class="brand"><span class="brand-mark"></span>Brevon Logistics</div>
      <div class="sender-address">17 Kolbe Street Meriton<br>Calderwood Harlen 0420<br>dirk@brevonlogistics.example</div>
    </div>
    <div class="headline">HEADLINE</div>
    <div class="letter-body">
      <p>Thank you for choosing us to move your freight. Our team plans every route with care so that each load arrives safely and on time.</p>
      <p>We offer road, warehouse and cross-border services backed by live tracking and a dedicated contact for every account.</p>
      <p>Please reach out with any questions about your next shipment.</p>
    </div>
    <div class="sign-off">
      <div class="signature">Dirk</div>
      <div class="card-name">Dirk Makhanya</div>
      <div class="card-title">Manager</div>
    </div>
    <div class="letterhead-footer">17 Kolbe Street Meriton · Calderwood Harlen 0420 · dirk@brevonlogistics.example</div>
  </div>

  <div class="piece envelope-back">
    <svg width="173" height="110" viewBox="0 0 173 110">
      <polygon points="0,0 173,0 86.5,52" fill="#1c1c1c"/>
      <polyline points="0,110 86.5,50 173,110" fill="none" stroke="#d6d6d6" stroke-width="1"/>
    </svg>
  </div>

  <div class="piece envelope-front">
    <div class="brand"><span class="brand-mark"></span>Brevon Logistics</div>
    <div class="sender-address">17 Kolbe Street Meriton<br>Calderwood Harlen 0420</div>
    <div class="envelope-window"></div>
  </div>

  <div class="piece notepad">
    <div class="notepad-binding"></div>
    <div class="brand"><span class="brand-mark"></span>Brevon Logistics</div>
  </div>

  <div class="disc"><div class="disc-hub"></div><div class="disc-hole"></div></div>

  <div class="lanyard"></div>
  <div class="piece badge">
    <div class="badge-clip"></div>
    <div class="card-name">Dirk Makhanya</div>
    <div class="card-title">Manager</div>
    <div class="brand"><span class="brand-mark"></span>Brevon Logistics</div>
  </div>

</body>
</html>
```